Business Card Design - Construction Company

Tarrowin Construction is in need of a sharp, modern business card design that has an architectural/high fashion feel.

We are looking for a two sided card.

One side simple dark grey/black with some texture in the background. e.g. (a mosaic of simple interconnecting shapes or a shadow of the logo.) Something to draw attention and create interest.It will need to feature a large Tarrowin construction logo (files attached) in metallic gradient or plain white.

The other side should contain all of our information:

(in largest text)
Name of person
Tarrowin Construction Pty. Ltd.

Licensed builders specialising in:
- Bathrooms
- Kitchens
- Commercial interiors

(mid sized text)
Phone number
Fax number
person@tarrowinconstruction.example.au
www. tarrowinconstruction.example.au

(smaller text)
ABN: 62407938215
BSA license: xxx-xxxx
PO Box 8641 Kellsmoor QLD 4019 (address)

Target Market(s)

professional home and business owners

Industry/Entity Type

Construction

Requirements
Must have
• Must be bold, professional looking and modern.
Nice to have
• We are undecided as to what kind of printing we will go with.
Definitely square edged.
Probably high quality satin card.
We are also interested in designs that would work well on transparent or translucent plastic.
Ideally we would print two versions.
Should not have
• Nothing with an antique feel.
No wild colours. Small amounts of colour can be good in the right place.

```html
<!DOCTYPE html>
<html lang="en">
<head>
<meta charset="utf-8">
<title>Business Card Design for Tarrowin Construction</title>
<link rel="stylesheet" href="https://fonts.googleapis.com/css2?family=Oswald:wght@300;400&family=Roboto+Condensed:wght@400;700&family=Montserrat:wght@500;600&display=swap">
<style>
  :root {
    --board-top: #f2f2f2;
    --board-bottom: #c9c9c9;
    --blue-light: #2f86d6;
    --blue-mid: #1d63b8;
    --blue-deep: #163f8f;
    --band: #1e1b1a;
    --accent-blue: #5ec3ff;
    --fine-blue: #86bdf0;
    --white: #ffffff;
    --back-dark: #2b2928;
    --back-darker: #1f1d1c;
    --silver: #c4c6c9;
    --rule: #a3a3a3;
    --title-slate: #4b5677;
    --title-dark: #242424;
    --label-grey: #7b7b7b;
  }
  * { margin: 0; padding: 0; box-sizing: border-box; }
  html, body { width: 1200px; height: 846px; overflow: hidden; }
  body {
    position: relative;
    background: linear-gradient(180deg, var(--board-top) 0%, var(--board-bottom) 100%);
    font-family: "Roboto Condensed", Arial, sans-serif;
  }
  .card {
    position: absolute;
    top: 175px;
    width: 290px;
    height: 509px;
    overflow: hidden;
    box-shadow: 3px 4px 8px rgba(0,0,0,0.28);
  }
  .card-front {
    left: 102px;
    background: radial-gradient(ellipse at 40% 35%, var(--blue-light) 0%, var(--blue-mid) 55%, var(--blue-deep) 100%);
    color: var(--white);
  }
  .front-corner-ring {
    position: absolute;
    top: -22px; right: 22px;
    width: 66px; height: 66px;
    border-radius: 50%;
    background: rgba(94,195,255,0.28);
  }
  .front-corner-square {
    position: absolute;
    bottom: 0; right: 12px;
    width: 70px; height: 70px;
    background: rgba(60,160,240,0.55);
  }
  .company-band {
    position: absolute;
    top: 63px; left: 0;
    width: 260px; height: 87px;
    background: var(--band);
    box-shadow: 2px 3px 5px rgba(0,0,0,0.35);
    padding: 44px 0 0 38px;
    font-family: "Montserrat", Arial, sans-serif;
    font-weight: 500;
  }
  .company-name { font-size: 15px; letter-spacing: 2px; line-height: 18px; }
  .company-legal { font-size: 9.5px; letter-spacing: 1.6px; line-height: 14px; }
  .services { position: absolute; top: 164px; left: 37px; }
  .services-title { color: var(--accent-blue); font-weight: 700; font-size: 13px; line-height: 16px; }
  .services-list { list-style: none; font-size: 12px; line-height: 16.5px; }
  .person-name {
    position: absolute; top: 272px; left: 36px;
    font-weight: 700; font-size: 24px;
  }
  .contact { position: absolute; top: 307px; left: 37px; font-size: 11px; line-height: 17px; }
  .fine-print {
    position: absolute; top: 410px; left: 37px;
    font-family: Arial, sans-serif;
    font-size: 8.5px; line-height: 15.5px; color: var(--fine-blue);
  }

  .card-back {
    left: 452px;
    background: radial-gradient(ellipse at 50% 50%, var(--back-dark) 0%, var(--back-darker) 100%);
  }
  .back-texture { position: absolute; inset: 0; }
  .back-mark {
    position: absolute; top: 180px; left: 0; width: 100%;
    text-align: center; color: var(--silver);
    font-family: "Montserrat", Arial, sans-serif; font-weight: 600;
  }
  .back-mark-dot {
    width: 70px; height: 70px; border-radius: 50%;
    background: var(--silver); margin: 0 auto 34px;
  }
  .back-mark-name { font-size: 24px; letter-spacing: 2px; line-height: 26px; }
  .back-mark-sub { font-size: 9px; letter-spacing: 1.5px; line-height: 14px; }

  .rule { position: absolute; left: 815px; width: 318px; height: 2px; background: var(--rule); }
  .rule-top { top: 177px; }
  .rule-bottom { top: 299px; }
  .board-title {
    position: absolute; top: 192px; left: 821px;
    font-family: "Oswald", Arial, sans-serif; font-weight: 300;
  }
  .board-kicker { color: var(--title-slate); font-size: 27px; line-height: 38px; }
  .board-kicker small { font-size: 18px; }
  .board-client { color: var(--title-dark); font-size: 40px; line-height: 50px; }
  .board-variant {
    position: absolute; top: 641px; left: 821px;
    font-family: "Oswald", Arial, sans-serif; font-weight: 300;
    font-size: 40px; color: var(--label-grey);
  }
</style>
</head>
<body>
  <section class="card card-front">
    <div class="front-corner-ring"></div>
    <div class="front-corner-square"></div>
    <div class="company-band">
      <div class="company-name">TARROWIN</div>
      <div class="company-legal">CONSTRUCTION PTY. LTD.</div>
    </div>
    <div class="services">
      <p class="services-title">Licensed builders specialising in:</p>
      <ul class="services-list">
        <li>- Bathrooms</li>
        <li>- Kitchens</li>
        <li>- Commercial interiors</li>
      </ul>
    </div>
    <h1 class="person-name">John Doe</h1>
    <div class="contact">
      <p>{P}&nbsp; 0400 5172 93</p>
      <p>{F}&nbsp; 0800 6291 47</p>
      <p>{E}&nbsp; person@tarrowinconstruction.example.au</p>
      <p>{W}&nbsp; www. tarrowinconstruction.example.au</p>
    </div>
    <div class="fine-print">
      <p>ABN: 62407938215</p>
      <p>BSA license: xxx-xxxx</p>
      <p>PO Box 8641 Kellsmoor QLD 4019</p>
    </div>
  </section>

  <section class="card card-back">
    <div class="back-texture" role="img" aria-label="Subtle repeating tonal pattern on dark charcoal background"></div>
    <div class="back-mark">
      <div class="back-mark-dot"></div>
      <div class="back-mark-name">TARROWIN</div>
      <div class="back-mark-sub">CONSTRUCTION</div>
    </div>
  </section>

  <div class="rule rule-top"></div>
  <div class="board-title">
    <p class="board-kicker">Business Card Design <small>for</small></p>
    <p class="board-client">Tarrowin Construction</p>
  </div>
  <div class="rule rule-bottom"></div>
  <p class="board-variant">Type A - i</p>
</body>
</html>
```